Stonefield Partners Business Card Design

We are looking for a new business card design, we are not happy with our current design. We are a boutique management consulting firm and our clients are typically fortune 500 companies.

I have attached the current front and back that we have as well as a version of our logo that can be used. I am trying to get a higher resolution version of the logo file to upload to the project.

Target Market(s)

Fortune 500 companies are our primary client base. Financial services, life sciences, pharmaceuticals and telecom companies are

Industry/Entity Type

Management Consulting

Contact Information for Business Card

We are trying to communicate a high degree of professionalism, a somewhat minimalist perhaps with some air of whimsy (without overdoing it). Attached is the current design, front and back as well as logos. I like the current back of the card and assume we will keep the phrase the same.

From a color palette perspective, I prefer to stay with a gray scale as they are today.

Font styles to use
Sans Serif

Colors
1b1b1b
474747
ffffff

Requirements
Must have
• Two sided business card design. File format should be something that can be used outside of Photoshop like MS Publisher so that they can be edited with personal information.
• Font should be calibri or something very similar and should be available within MS Office
Should not have
• No other logos or graphics outside of the logo provided.

```html
<!DOCTYPE html>
<html lang="en">
<head>
<meta charset="utf-8">
<title>Stonefield Partners – Business Card</title>
<link rel="stylesheet" href="https://fonts.googleapis.com/css2?family=Carlito:ital,wght@0,400;0,700;1,400&family=Open+Sans:wght@300;400;700&display=swap">
<style>
  :root {
    --ink: #000000;
    --charcoal: #1b1b1b;
    --slate: #474747;
    --paper: #ffffff;
    --backdrop: #e9eaea;
  }
  * { box-sizing: border-box; margin: 0; padding: 0; }
  html, body {
    width: 1200px; height: 900px; overflow: hidden;
    background: var(--backdrop);
    font-family: "Carlito", "Calibri", sans-serif;
  }
  .sheet {
    width: 1200px; height: 900px;
    display: flex; flex-direction: column; align-items: center; justify-content: center;
    gap: 50px;
  }
  .card {
    width: 630px; height: 360px;
    box-shadow: 0 6px 18px rgba(0,0,0,.18);
    position: relative; overflow: hidden;
    color: var(--paper);
  }

  /* Front */
  .card-front { background: var(--ink); display: grid; grid-template-rows: 205px 1fr; }
  .front-top { display: flex; justify-content: space-between; padding: 22px 28px 0 40px; }
  .front-mark { display: flex; align-items: center; gap: 10px; align-self: center; margin-top: -14px; }
  .mark-dot { width: 34px; height: 34px; border-radius: 50%; background: var(--paper); flex: none; }
  .mark-name { font-size: 34px; font-weight: 700; color: var(--paper); }
  .identity { text-align: center; }
  .person-name {
    font-family: "Open Sans", sans-serif; font-size: 38px; line-height: 1; margin-bottom: 28px;
  }
  .person-name .first { font-weight: 700; }
  .person-name .last { font-weight: 400; }
  .role-line { font-size: 18px; line-height: 1.25; }
  .role-line.company { font-weight: 700; }
  .front-bottom { display: grid; grid-template-columns: 50% 50%; }
  .office-block {
    background: var(--paper); color: var(--ink);
    text-align: center; font-size: 18px; line-height: 1.3;
    padding-top: 8px; font-style: normal;
  }
  .office-block .company { font-weight: 700; }
  .contact-block {
    background: var(--charcoal); text-align: center;
    font-size: 18px; line-height: 1.35; padding-top: 20px;
  }
  .contact-block .web { font-weight: 700; }

  /* Back */
  .card-back {
    background: var(--ink);
    display: flex; flex-direction: column; align-items: center; justify-content: center;
  }
  .back-mark { display: flex; align-items: center; gap: 14px; margin-top: 10px; }
  .back-mark .mark-dot { width: 66px; height: 66px; }
  .back-mark .mark-name { font-size: 82px; font-weight: 400; line-height: 1; }
  .tm { font-size: 14px; align-self: flex-start; margin-left: -8px; margin-top: 2px; }
  .tagline {
    margin-top: 42px; text-align: center;
    font-family: "Open Sans", sans-serif; font-size: 27px; line-height: 1.35; font-weight: 300;
  }
</style>
</head>
<body>
<main class="sheet">
  <section class="card card-front" aria-label="Card front">
    <div class="front-top">
      <div class="front-mark">
        <span class="mark-dot"></span>
        <span class="mark-name">Stonefield</span>
      </div>
      <div class="identity">
        <p class="person-name"><span class="first">Mark</span><span class="last">Ellison</span></p>
        <p class="role-line">Los Angeles Office</p>
        <p class="role-line">Managing Director</p>
        <p class="role-line company">Stonefield Partners, Inc.</p>
      </div>
    </div>
    <div class="front-bottom">
      <address class="office-block">
        <p class="company">Stonefield Partners, Inc.</p>
        <p>Headquarters</p>
        <p>218 Harbor View Road</p>
        <p>Suite 210</p>
        <p>Cedar Point, WA 98000</p>
      </address>
      <div class="contact-block">
        <p>555.014.2290</p>
        <p>mellison@stonefieldpartners.com</p>
        <p class="web">www.StonefieldPartners.com</p>
      </div>
    </div>
  </section>

  <section class="card card-back" aria-label="Card back">
    <div class="back-mark">
      <span class="mark-dot"></span>
      <span class="mark-name">Stonefield</span>
      <span class="tm">™</span>
    </div>
    <p class="tagline">The trusted partner<br>for leadership’s boldest agendas</p>
  </section>
</main>
</body>
</html>
```